Public Relations Agency Seeks Wordpress Design and Coding

TORVEX Media is a public relations agency specializing in media relations, public affairs and marketing communication.

The site should display the following visual characteristics: professionalism, trustworthiness, high-tech focus, clear and concise design.

The desired colors are royal blue, gray and hints of red.

Design look/feel inspired by this site: http://brisklanefetes.example/

Specifications:

1. Navigation/Pages/Index:

HOME

ABOUT US

SERVICES

NEWS

CONTACT

---

2. Functionality of/content for each page:

- Home
o Dominant photo (professional, edgy, innovative)
o Simple, straightforward access to/from “Home” from other pages
o Includes logo (attached) and tagline "Unleash the power of communication"
o Direct link to “CONTACT”
o Links to social media accounts: Facebook, Twitter, LinkedIn

- About Us

o Company profile blurb
o President’s photo with short bio

- Services
o Public Relations
 Strategic communication
 Brand and reputation management
 Community relations
o Media Relations
 News coverage and contacts
 Media training and interview skills
 Crisis communications
o Congressional Affairs
 Public affairs
 Public policy
 Legislative strategy
o Mass Communication
 Speechwriting
 Presentation creation
 Social media
o Marketing Communications
 Business collateral material
 Promotional campaigns
 Special events and tradeshows

- News
o Blog-like page to post information and/or share news from other sites

- Contact
o Standard “Contact Us” form (Name, Email, Phone, Message)
o Direct Contact
 (555) 314-2690
 Marlow@TORVEXmedia.example

Target Market(s)

Small to large businesses specializing in high technology, defense/military, medicine/healthcare, and wide array of professional services.

Industry/Entity Type

Marketing

Font styles to use
Serif
Sans Serif

Colors
0555a3
ec2027
edf3f7

Requirements
Must have
• -- Project reqires DESIGN - and - fully CODED.

-- Strong SEO

-- Optimized for mobile viewing

Thank you!

```html
<!DOCTYPE html>
<html lang="en">
<head>
<meta charset="utf-8">
<title>TORVEX Media</title>
<link href="https://fonts.googleapis.com/css2?family=Open+Sans:wght@300;400;700&family=Raleway:wght@400;500&display=swap" rel="stylesheet">
<style>
  :root {
    --royal-blue: #1f5aa6;
    --link-blue: #1d4fa8;
    --accent-red: #d9413b;
    --header-gray: rgba(92, 92, 92, 0.93);
    --tagline-bg: rgba(120, 128, 150, 0.6);
    --ink: #2f2f2f;
    --muted: #6b6b6b;
    --rule: #e3e6e8;
    --card-bg: #f6f8fa;
    --card-border: #e8ecef;
    --white: #ffffff;
  }
  * { box-sizing: border-box; margin: 0; padding: 0; }
  html, body { width: 1200px; height: 871px; overflow: hidden; background: var(--white); }
  body { position: relative; font-family: "Open Sans", Arial, sans-serif; }

  .hero {
    position: absolute; left: 0; top: 0; width: 1200px; height: 599px;
    background:
      radial-gradient(ellipse 260px 220px at 120px 200px, rgba(70,110,50,0.75), transparent 70%),
      radial-gradient(ellipse 300px 300px at 1040px 220px, rgba(40,70,40,0.85), transparent 70%),
      radial-gradient(ellipse 330px 260px at 590px 400px, rgba(190,195,200,0.9), transparent 72%),
      linear-gradient(135deg, #6a3018 0%, #7a3a1c 45%, #5a2a16 100%);
  }

  .site-header {
    position: absolute; left: 0; top: 0; width: 1200px; height: 61px;
    background: var(--header-gray);
  }
  .brand {
    position: absolute; left: 148px; top: 0; width: 194px; height: 61px;
    background: var(--royal-blue);
    display: flex; align-items: center; justify-content: center;
    color: var(--white); font-weight: 700; font-size: 24px; letter-spacing: 0.5px;
    text-decoration: none;
  }
  .main-nav a {
    position: absolute; top: 16px; color: var(--white); text-decoration: none;
    font-weight: 300; font-size: 23px; line-height: 30px;
  }

  .tagline {
    position: absolute; left: 150px; top: 283px; width: 352px; height: 105px;
    background: var(--tagline-bg);
    padding: 6px 8px; color: var(--white);
    font-size: 35px; line-height: 45px; font-weight: 400;
  }
  .tagline strong { font-weight: 700; }

  .slider-arrow { position: absolute; top: 318px; width: 16px; height: 26px; }
  .slider-arrow.prev { left: 94px; }
  .slider-arrow.next { left: 1139px; }

  .social-tabs { position: absolute; left: 1165px; top: 280px; width: 35px; }
  .social-tabs span {
    display: block; width: 35px; height: 29px; margin-bottom: 2px; background: var(--accent-red);
  }

  .promo { position: absolute; left: 158px; top: 640px; width: 885px; }
  .promo h2 {
    font-family: "Raleway", Arial, sans-serif; font-weight: 400; font-size: 28px;
    color: var(--ink); line-height: 42px;
  }
  .promo h2 em { font-style: normal; color: var(--link-blue); }
  .promo p {
    font-family: "Raleway", Arial, sans-serif; font-size: 13px; color: var(--muted); margin-top: 0;
  }
  .promo-button {
    position: absolute; left: 909px; top: 653px; width: 134px; height: 38px;
    background: var(--accent-red); display: block;
  }
  .divider { position: absolute; left: 158px; top: 728px; width: 885px; height: 1px; background: var(--rule); }

  .feature {
    position: absolute; top: 791px; width: 285px; height: 100px;
    background: var(--card-bg); border: 1px solid var(--card-border);
    font-family: "Raleway", Arial, sans-serif; font-size: 17px; color: var(--ink);
    text-align: center; padding-top: 45px;
  }
</style>
</head>
<body>
  <div class="hero" role="img" aria-label="Top view of an open laptop on a wooden desk surrounded by potted plants and a coffee cup"></div>

  <header class="site-header">
    <a class="brand" href="#">TORVEX Media</a>
    <nav class="main-nav">
      <a href="#" style="left:519px">Home</a>
      <a href="#" style="left:616px">About Us</a>
      <a href="#" style="left:746px">Services</a>
      <a href="#" style="left:871px">News</a>
      <a href="#" style="left:956px">Contact</a>
    </nav>
  </header>

  <h1 class="tagline">Unleash the power<br>of <strong>communication</strong></h1>

  <svg class="slider-arrow prev" viewBox="0 0 16 26"><polyline points="13,2 3,13 13,24" fill="none" stroke="#fff" stroke-width="2"/></svg>
  <svg class="slider-arrow next" viewBox="0 0 16 26"><polyline points="3,2 13,13 3,24" fill="none" stroke="#fff" stroke-width="2"/></svg>

  <div class="social-tabs"><span></span><span></span><span></span></div>

  <section class="promo">
    <h2>Hear more about our <em>new promotion</em></h2>
    <p>We care not only to create quality themes, but as well make sure users succeed to setup, easy to use admin interface.</p>
  </section>
  <a class="promo-button" href="#" aria-label="Learn more"></a>
  <div class="divider"></div>

  <div class="feature" style="left:158px">Responsive Ready</div>
  <div class="feature" style="left:458px">Powerful Admin</div>
  <div class="feature" style="left:758px">Deeply Customizable</div>
</body>
</html>
```